Construction machinery rental / heavy equipment rental needs a nice billboard

We need a billboard for our company.
We rent out construction machinery such as excavators, wheel loaders, wheel dumpers and so on...

I would like an elegant, simple, dark design.
Colors: black yellow grey white

The following must be on the billboard:
Logo
phone number: 076 / 913 58 40
website: www.geraetepark-lorvento.ch
the machines I rent out: Bagger bis 10T, Radlader, Dumper, Raupenkipper

the font in the logo is: Square 721

Final format 2950 x 1900mm
I have uploaded pictures:
"Excavator 1-6" are my pictures, which can be used
"Sample 1-4" are pictures whose style I like
"Billboard" are billboards which I like

Requirements
Must have
• The following must be on the billboard: Logo phone number: 076 / 913 58 40 website: www.geraetepark-lorvento.ch the machines I rent out: Bagger bis 10T, Radlader, Dumper, Raupenkipper

```html
<!DOCTYPE html>
<html lang="de">
<head>
<meta charset="utf-8">
<title>Lorvento Baumaschinenvermietung – Plakat</title>
<link rel="stylesheet" href="https://fonts.googleapis.com/css2?family=Michroma&family=Rubik:wght@400;500;800&display=swap">
<style>
  :root {
    --page: #a3a3a3;
    --black: #050505;
    --white: #ffffff;
    --yellow: #e9d236;
    --yellow-dark: #cdb52a;
    --grey-dark: #2b2b2b;
    --grey-mid: #5a5a5a;
    --photo-light: #8a8a8a;
    --photo-mid: #4a4a4a;
    --photo-deep: #1c1c1c;
  }
  html, body {
    margin: 0;
    padding: 0;
    width: 880px;
    height: 1200px;
    overflow: hidden;
    background: var(--page);
  }
  .billboard {
    position: absolute;
    left: 30px;
    top: 336px;
    width: 820px;
    height: 528px;
    background: var(--black);
    overflow: hidden;
    font-family: "Michroma", sans-serif;
    color: var(--white);
  }
  .machine-photo {
    position: absolute;
    left: 313px;
    top: 18px;
    width: 507px;
    height: 448px;
    background:
      radial-gradient(ellipse 26% 18% at 22% 84%, var(--photo-light) 0%, rgba(90,90,90,0.6) 45%, rgba(5,5,5,0) 100%),
      radial-gradient(ellipse 32% 16% at 80% 80%, var(--photo-light) 0%, rgba(90,90,90,0.55) 50%, rgba(5,5,5,0) 100%),
      radial-gradient(ellipse 22% 30% at 88% 52%, #6e6e6e 0%, rgba(70,70,70,0.5) 50%, rgba(5,5,5,0) 100%),
      radial-gradient(ellipse 14% 45% at 22% 45%, #5c5c5c 0%, rgba(60,60,60,0.5) 55%, rgba(5,5,5,0) 100%),
      radial-gradient(ellipse 45% 14% at 45% 12%, #555 0%, rgba(60,60,60,0.4) 55%, rgba(5,5,5,0) 100%),
      radial-gradient(ellipse 60% 60% at 58% 48%, var(--photo-mid) 0%, var(--photo-deep) 55%, rgba(5,5,5,0) 100%);
  }
  .brand {
    position: absolute;
    left: 48px;
    top: 74px;
    display: flex;
    align-items: center;
    gap: 12px;
  }
  .brand-mark {
    width: 28px;
    height: 28px;
    border-radius: 50%;
    background: var(--yellow);
  }
  .brand-name {
    font-family: "Michroma", sans-serif;
    font-size: 33px;
    color: var(--yellow);
    letter-spacing: 1px;
  }
  .headline {
    position: absolute;
    left: 46px;
    top: 172px;
    margin: 0;
    font-size: 31px;
    font-weight: 400;
    letter-spacing: 0.5px;
    line-height: 1.2;
  }
  .machine-list {
    position: absolute;
    left: 46px;
    top: 234px;
    margin: 0;
    padding: 0;
    list-style: none;
  }
  .machine-list li {
    display: flex;
    align-items: center;
    height: 35px;
    font-size: 16.5px;
  }
  .machine-list svg {
    width: 10px;
    height: 10px;
    margin-right: 10px;
  }
  .footer-band {
    position: absolute;
    left: 0;
    top: 0;
    width: 820px;
    height: 528px;
  }
  .phone {
    position: absolute;
    left: 40px;
    top: 460px;
    height: 68px;
    display: flex;
    align-items: center;
    gap: 10px;
    font-family: "Rubik", sans-serif;
    font-weight: 800;
    font-size: 35px;
    color: var(--black);
  }
  .phone svg {
    width: 25px;
    height: 25px;
  }
  .website {
    position: absolute;
    left: 420px;
    width: 390px;
    top: 460px;
    height: 68px;
    display: flex;
    align-items: center;
    justify-content: center;
    font-family: "Rubik", sans-serif;
    font-weight: 500;
    font-size: 22px;
    color: var(--white);
  }
</style>
</head>
<body>
  <main class="billboard">
    <div class="machine-photo" role="img" aria-label="Schwarzweissfoto eines Minibaggers mit Tieflöffel und Planierschild"></div>

    <div class="brand">
      <span class="brand-mark"></span>
      <span class="brand-name">LORVENTO</span>
    </div>

    <h1 class="headline">VERMIETUNG</h1>

    <ul class="machine-list">
      <li><svg viewBox="0 0 10 10"><path d="M1 1 L5 5 L1 9 M5 1 L9 5 L5 9" fill="none" stroke="#e9d236" stroke-width="1.6"/></svg>BAGGER BIS 10T</li>
      <li><svg viewBox="0 0 10 10"><path d="M1 1 L5 5 L1 9 M5 1 L9 5 L5 9" fill="none" stroke="#e9d236" stroke-width="1.6"/></svg>RADLADER</li>
      <li><svg viewBox="0 0 10 10"><path d="M1 1 L5 5 L1 9 M5 1 L9 5 L5 9" fill="none" stroke="#e9d236" stroke-width="1.6"/></svg>DUMPER</li>
      <li><svg viewBox="0 0 10 10"><path d="M1 1 L5 5 L1 9 M5 1 L9 5 L5 9" fill="none" stroke="#e9d236" stroke-width="1.6"/></svg>RAUPENKIPPER</li>
    </ul>

    <svg class="footer-band" viewBox="0 0 820 528" aria-hidden="true">
      <defs>
        <linearGradient id="yellowBand" x1="0" y1="0" x2="1" y2="0">
          <stop offset="0" stop-color="#e9d236"/>
          <stop offset="1" stop-color="#d9c130"/>
        </linearGradient>
        <linearGradient id="greyBand" x1="0" y1="0" x2="0" y2="1">
          <stop offset="0" stop-color="#5a5a5a"/>
          <stop offset="1" stop-color="#2b2b2b"/>
        </linearGradient>
      </defs>
      <polygon points="402,463 820,463 820,528 380,528" fill="url(#greyBand)"/>
      <polygon points="0,460 411,460 386,528 0,528" fill="url(#yellowBand)"/>
    </svg>

    <div class="phone">
      <svg viewBox="0 0 24 24"><circle cx="12" cy="12" r="12" fill="#050505"/><path d="M8.2 6.5c.4-.4 1-.4 1.3 0l1.3 1.6c.3.4.3.9 0 1.2l-.8.8c.6 1.3 1.6 2.4 2.9 3l.8-.8c.3-.3.9-.4 1.2 0l1.6 1.3c.4.3.4.9 0 1.3l-.9.9c-.7.7-1.8.8-2.7.3-2.4-1.3-4.2-3.2-5.5-5.5-.5-.9-.4-2 .3-2.7z" fill="#e9d236"/></svg>
      <span>076 / 913 58 40</span>
    </div>

    <div class="website">geraetepark-lorvento.ch</div>
  </main>
</body>
</html>
```